Business Card Design

Provide project management services to the construction and other industries
Construction services - Civil and Concrete works
Shop Detailing
Structural Modelling
Client side coordination of project teams and consultants
Feasibility Studies for construction projects

Industry/Entity Type

Business

Contact Information for Business Card

Crestline Ops
Darrel Pikett B.Sc (Eng), M.ProjMgt
Principal

m: 0412 583 716
e: dpikett@crestlineops.com.au

p: 08 6293 4078
a: 17 Bramblewood Court, Hallsbury, WA 6048

```html
<!DOCTYPE html>
<html lang="en">
<head>
<meta charset="utf-8">
<title>Crestline Ops – Business Card</title>
<link rel="stylesheet" href="https://fonts.googleapis.com/css2?family=Source+Sans+3:wght@400;600;800&display=swap">
<style>
  :root {
    --backdrop: #4a4a4a;
    --card-white: #ffffff;
    --brand-green: #007f00;
    --rule-dark: #1e1e1e;
    --ink: #111111;
    --text-grey: #4d4d4d;
  }
  html, body {
    margin: 0;
    width: 1105px;
    height: 1200px;
    overflow: hidden;
    background: var(--backdrop);
    font-family: "Source Sans 3", Arial, sans-serif;
  }
  .card {
    position: absolute;
    left: 196px;
    width: 720px;
    height: 412px;
    box-shadow: 0 3px 8px rgba(0,0,0,0.45);
    overflow: hidden;
  }
  .card-front { top: 146px; background: var(--card-white); }
  .card-back { top: 602px; height: 410px; background: var(--brand-green); }

  .wordmark {
    position: absolute;
    left: 0; right: 0;
    text-align: center;
    font-weight: 800;
    font-size: 50px;
    letter-spacing: 4px;
    line-height: 1;
    white-space: nowrap;
  }
  .card-front .wordmark { top: 80px; color: var(--ink); }
  .card-back .wordmark { top: 182px; color: var(--ink); }

  .rule {
    position: absolute;
    left: 0; right: 0;
    height: 3px;
    background: var(--rule-dark);
  }
  .rule-top { top: 189px; }
  .rule-bottom { top: 283px; }

  .name-band {
    position: absolute;
    left: 0; right: 0;
    top: 196px;
    height: 83px;
    background: var(--brand-green);
    color: var(--card-white);
    text-align: center;
  }
  .person-name {
    position: absolute;
    left: 0; right: 0; top: 12px;
    font-size: 25px;
    font-weight: 600;
    white-space: nowrap;
  }
  .credentials { font-size: 19px; font-weight: 400; }
  .role {
    position: absolute;
    left: 0; right: 0; top: 49px;
    font-size: 20px;
  }

  .contact {
    position: absolute;
    left: 0; right: 0;
    text-align: center;
    font-size: 19px;
    color: var(--text-grey);
    line-height: 27px;
    white-space: nowrap;
  }
  .contact-row-1 { top: 330px; }
  .contact-row-2 { top: 357px; }
  .label { color: var(--brand-green); font-weight: 600; }

  .web-address {
    position: absolute;
    left: 0; right: 0; top: 346px;
    text-align: center;
    color: var(--card-white);
    font-size: 20px;
    letter-spacing: 3.5px;
  }
</style>
</head>
<body>
  <section class="card card-front">
    <div class="wordmark">CRESTLINE OPS</div>
    <div class="rule rule-top"></div>
    <div class="name-band">
      <div class="person-name">DARREL PIKETT <span class="credentials">B.Sc (Eng), M.ProjMgt</span></div>
      <div class="role">Principal</div>
    </div>
    <div class="rule rule-bottom"></div>
    <div class="contact contact-row-1">17 Bramblewood Court, Hallsbury, WA 6048 <span class="label">|</span> <span class="label">P:</span> 08 6293 4078 &nbsp;<span class="label">M:</span> 0412 583 716</div>
    <div class="contact contact-row-2"><span class="label">E:</span> dpikett@crestlineops.com.au &nbsp;<span class="label">W:</span> www.crestlineops.com.au</div>
  </section>

  <section class="card card-back">
    <div class="wordmark">CRESTLINE OPS</div>
    <div class="web-address">www.crestlineops.com.au</div>
  </section>
</body>
</html>
```